Brightstone Roofing Business Card

This is my current business card. But I’d like to make some changes. Somewhere on the card I’d like to list some of the services we offer. Maybe on the back? But I’d still like to keep the red. White and black modern look.

-residential & commercial roofing
-Roof Repairs & Maintenance
-Storm Damage & Insurance Claims specialist
-Christmas Lights and permanent Christmas lights
Fencing. Windows. Gutters. Siding. Sheetrock, painting.

```html
<!DOCTYPE html>
<html lang="en">
<head>
<meta charset="utf-8">
<title>Brightstone Roofing Business Card</title>
<link rel="stylesheet" href="https://fonts.googleapis.com/css2?family=Michroma&family=Arimo:wght@400;700&display=swap">
<style>
  :root {
    --backdrop: #3d3d3d;
    --card: #030303;
    --red: #e3101b;
    --white: #ffffff;
    --grey: #cfcfcf;
  }
  * { box-sizing: border-box; margin: 0; padding: 0; }
  html, body {
    width: 1200px;
    height: 803px;
    overflow: hidden;
    background: var(--backdrop);
  }
  .stage {
    position: relative;
    width: 1200px;
    height: 803px;
  }
  .card {
    position: absolute;
    top: 258px;
    width: 500px;
    height: 286px;
    background: var(--card);
    border-radius: 18px;
    border-bottom: 3px solid var(--red);
    box-shadow: 0 18px 30px rgba(0,0,0,0.45);
    overflow: hidden;
  }
  .card--front { left: 70px; }
  .card--back { left: 630px; }

  .brand-mark {
    display: block;
    border-radius: 50%;
    background: var(--red);
    border: 3px solid var(--white);
  }
  .brand-name {
    font-family: "Michroma", sans-serif;
    color: var(--white);
    font-weight: 400;
    line-height: 1.25;
    letter-spacing: 0.02em;
  }

  /* front */
  .front-brand {
    position: absolute;
    top: 34px;
    right: 36px;
    display: flex;
    flex-direction: column;
    align-items: center;
    gap: 12px;
  }
  .front-brand .brand-mark { width: 86px; height: 86px; }
  .front-brand .brand-name { font-size: 15px; text-align: center; }

  .contact {
    position: absolute;
    left: 36px;
    bottom: 34px;
  }
  .contact__name {
    font-family: "Michroma", sans-serif;
    color: var(--red);
    font-size: 20px;
    font-weight: 400;
    letter-spacing: 0.04em;
  }
  .contact__role {
    font-family: "Arimo", sans-serif;
    color: var(--white);
    font-size: 11.5px;
    margin-top: 4px;
  }
  .contact__list {
    list-style: none;
    margin-top: 16px;
    display: flex;
    flex-direction: column;
    gap: 5px;
  }
  .contact__item {
    display: flex;
    align-items: center;
    gap: 10px;
    font-family: "Arimo", sans-serif;
    color: var(--white);
    font-size: 11.5px;
  }
  .contact__icon { width: 12px; height: 12px; flex: none; }

  /* back */
  .back-layout {
    position: absolute;
    inset: 0;
    padding: 20px 28px 18px;
    display: flex;
    flex-direction: column;
    align-items: center;
  }
  .back-layout .brand-mark { width: 58px; height: 58px; }
  .back-layout .brand-name {
    font-size: 15px;
    text-align: center;
    margin-top: 8px;
  }
  .services {
    width: 100%;
    margin-top: 12px;
    padding-top: 10px;
    border-top: 1px solid var(--red);
  }
  .services__list {
    list-style: none;
    display: grid;
    grid-template-columns: 1fr 1fr;
    column-gap: 14px;
    row-gap: 5px;
  }
  .services__item {
    display: flex;
    align-items: center;
    gap: 7px;
    font-family: "Arimo", sans-serif;
    font-size: 10.5px;
    color: var(--white);
    white-space: nowrap;
  }
  .services__item::before {
    content: "";
    width: 5px;
    height: 5px;
    background: var(--red);
    flex: none;
  }
  .services__trades {
    margin-top: 7px;
    font-family: "Arimo", sans-serif;
    font-size: 10.5px;
    color: var(--grey);
    text-align: center;
    letter-spacing: 0.02em;
  }
  .back-layout__web {
    margin-top: auto;
    font-family: "Arimo", sans-serif;
    color: var(--white);
    font-size: 11.5px;
  }
</style>
</head>
<body>
<main class="stage">

  <section class="card card--front" aria-label="Card front">
    <div class="front-brand">
      <span class="brand-mark" aria-hidden="true"></span>
      <p class="brand-name">Brightstone<br>Roofing Co.</p>
    </div>

    <div class="contact">
      <h1 class="contact__name">DALE MERCER</h1>
      <p class="contact__role">Roofing Contractor in Texas</p>
      <ul class="contact__list">
        <li class="contact__item">
          <svg class="contact__icon" viewBox="0 0 24 24" aria-hidden="true"><path fill="var(--red)" d="M6.6 10.8a15.1 15.1 0 0 0 6.6 6.6l2.2-2.2a1 1 0 0 1 1-.25 11.4 11.4 0 0 0 3.6.57 1 1 0 0 1 1 1V20a1 1 0 0 1-1 1A17 17 0 0 1 3 4a1 1 0 0 1 1-1h3.5a1 1 0 0 1 1 1c0 1.250.2 2.450.57 3.6a1 1 0 0 1-.25 1z"/></svg>
          555.014.2290
        </li>
        <li class="contact__item">
          <svg class="contact__icon" viewBox="0 0 24 24" aria-hidden="true"><rect x="2" y="5" width="20" height="14" rx="2" fill="var(--red)"/><path d="M3 6l9 7 9-7" fill="none" stroke="var(--card)" stroke-width="2"/></svg>
          dale@brightstoneroofing.co
        </li>
        <li class="contact__item">
          <svg class="contact__icon" viewBox="0 0 24 24" aria-hidden="true"><circle cx="12" cy="12" r="10" fill="var(--red)"/><path d="M2 12h20M12 2c3 3 3 17 0 20M12 2c-3 3-3 17 0 20" fill="none" stroke="var(--card)" stroke-width="1.5"/></svg>
          www.brightstoneroofing.co
        </li>
      </ul>
    </div>
  </section>

  <section class="card card--back" aria-label="Card back">
    <div class="back-layout">
      <span class="brand-mark" aria-hidden="true"></span>
      <p class="brand-name">Brightstone<br>Roofing Co.</p>

      <div class="services">
        <ul class="services__list">
          <li class="services__item">Residential &amp; Commercial Roofing</li>
          <li class="services__item">Roof Repairs &amp; Maintenance</li>
          <li class="services__item">Storm Damage &amp; Insurance Claims</li>
          <li class="services__item">Christmas &amp; Permanent Lights</li>
        </ul>
        <p class="services__trades">Fencing · Windows · Gutters · Siding · Sheetrock · Painting</p>
      </div>

      <p class="back-layout__web">www.brightstoneroofing.co</p>
    </div>
  </section>

</main>
</body>
</html>
```